Brightmoor Learning Trifold Flyer

Brightmoor is an award-winning organisation providing dynamic and creative ways for children, young people, adults and families to make positive change and achieve fulfilling lives.
Brightmoor offers a range of learning solutions focussed on supporting and empowering Individuals and organisations that support people with a range of disabilities. We have 3 core areas of the business - Therapy, Support and Learning.
This flyer is focussed on the learning area of our business - Brightmoor offers a range of learning solutions focussed on supporting and empowering Individuals and organisations that support people with a range of disabilities.
For this flyers we are after an a4 colour double sided flyer in either a A4 tri-fold to DL format or A4 bi-fold to A5 format. We are looking for a design that is simple and dynamic whilst keeping in line with our branding.
The winning designs will need to be hi-res and ready for print and also a lower res version suitable to email.
I have attached a number of files to provide further background, including:
• I have attached a word doc of copy for the flyer
• Brand Guidelines
• Logo
• Our clinic flyer recently produced by a ArtPlenty designer for our clinic area of the business. These flyers do not have to be exactly the same as this one but should appear to be from the same organisation although a different service.
Generally we like our designs to be clear and simple.
Please don't hesitate to reach out with any Q's.

```html
<!DOCTYPE html>
<html lang="en">
<head>
<meta charset="utf-8">
<title>Brightmoor Learning Trifold Flyer</title>
<link href="https://fonts.googleapis.com/css2?family=Montserrat:wght@500;600;700;800&family=Oswald:wght@500;600&family=Open+Sans:wght@400;600;700&display=swap" rel="stylesheet">
<style>
:root{
  --sage:#6f9a86;
  --sage-dark:#5a8571;
  --sage-light:#dfe8e3;
  --salmon:#d8a899;
  --ink:#4a4d4c;
  --muted:#7b7f7d;
  --paper:#ffffff;
  --paper-soft:#f3f3f1;
  --backdrop:#e6e6e4;
  --photo-dark:#6e6e6e;
  --photo-light:#c9c9c9;
}
*{box-sizing:border-box;margin:0;padding:0}
html,body{width:1200px;height:3600px;overflow:hidden}
body{background:var(--backdrop);font-family:"Open Sans",Arial,sans-serif;color:var(--ink);
  display:flex;flex-direction:column;align-items:center;justify-content:center;gap:120px}
.spread{width:1120px;height:792px;display:grid;grid-template-columns:repeat(3,1fr);background:var(--paper);box-shadow:0 6px 24px rgba(0,0,0,.12)}
.panel{position:relative;overflow:hidden;padding:0 30px}
.photo{background:linear-gradient(135deg,var(--photo-light),var(--photo-dark));filter:grayscale(1)}
.wordmark{display:flex;align-items:center;gap:9px;font-family:"Montserrat",Arial,sans-serif;font-weight:700}
.wordmark .dot{width:22px;height:22px;border-radius:50%;background:currentColor}
.btn{display:block;text-align:center;font-family:"Montserrat",Arial,sans-serif;font-weight:600;letter-spacing:1.5px;font-size:13px;color:#fff;padding:9px 10px}
.btn.salmon{background:var(--salmon)}
.btn.sage{background:var(--sage)}
p.body{font-size:10.5px;line-height:1.6;color:var(--muted);margin-bottom:9px}
h2{font-family:"Montserrat",Arial,sans-serif;color:var(--sage);font-weight:700}
ul.list{list-style:none;font-size:10.5px;line-height:1.55;color:var(--muted)}
ul.list li{padding-left:14px;position:relative;margin-bottom:3px}
ul.list li::before{content:"";position:absolute;left:0;top:6px;width:6px;height:6px;background:var(--sage)}

/* outside spread */
.about .about-photo{position:absolute;left:0;top:0;width:100%;height:330px;clip-path:polygon(0 0,100% 0,100% 62%,72% 100%,0 100%)}
.about .about-band{position:absolute;right:0;top:190px;width:130px;height:160px;background:var(--sage);clip-path:polygon(100% 0,100% 100%,0 100%)}
.about .content{position:absolute;left:30px;right:30px;top:360px}
.about h2{font-size:22px;margin-bottom:14px}
.about h2 span{color:var(--ink);font-weight:800;font-size:13px;display:block;letter-spacing:2px}
.about .btn{margin-top:16px}

.contact{padding:0}
.contact .quote{padding:34px 34px 0;height:360px;text-align:center}
.contact .quote-mark{font-family:Georgia,serif;font-size:60px;color:var(--sage);line-height:.8}
.contact .quote p{font-size:10.5px;line-height:1.6;color:var(--muted);font-style:italic;margin-bottom:10px}
.contact .quote .cite{font-style:normal;font-weight:700;color:var(--sage)}
.contact .green{position:absolute;left:0;right:0;top:360px;bottom:0;background:var(--sage);padding:28px 34px;color:#fff}
.contact .green .wordmark{font-size:30px;color:#fff;justify-content:center;margin-bottom:18px}
.contact .phone{background:var(--salmon);text-align:center;font-family:"Montserrat",Arial,sans-serif;font-weight:700;font-size:22px;padding:8px;margin-bottom:18px;letter-spacing:1px}
.contact .rows{list-style:none;font-size:11px;line-height:1.4}
.contact .rows li{display:flex;gap:10px;align-items:flex-start;margin-bottom:9px}
.contact .rows svg{flex:none;width:18px;height:18px}
.contact .platform{text-align:center;font-size:10px;letter-spacing:1.5px;margin-top:14px;margin-bottom:6px;font-weight:600}
.contact .btn{background:#fff;color:var(--sage)}

.cover{padding:0}
.cover .cover-photo{position:absolute;left:0;top:0;width:100%;height:400px;clip-path:polygon(0 0,100% 0,100% 100%,0 78%)}
.cover .cover-band{position:absolute;left:0;top:300px;width:100%;height:120px;background:var(--sage-light);clip-path:polygon(0 0,100% 80%,100% 100%,0 100%)}
.cover .content{position:absolute;left:40px;right:40px;top:440px}
.cover .wordmark{font-size:34px;color:var(--sage)}
.cover h1{font-family:"Oswald",Arial,sans-serif;font-weight:600;color:var(--sage);font-size:62px;line-height:1;margin-top:22px;letter-spacing:1px}
.cover .tag{background:var(--salmon);color:#fff;font-size:11px;letter-spacing:2px;padding:6px 10px;margin-top:14px;font-family:"Montserrat",Arial,sans-serif;font-weight:600}
.cover .foot{position:absolute;left:0;right:0;bottom:0;background:var(--sage);color:#fff;text-align:center;font-family:"Montserrat",Arial,sans-serif;font-weight:600;letter-spacing:2px;font-size:15px;padding:16px}

/* inside spread */
.offers .lead{font-family:"Montserrat",Arial,sans-serif;color:var(--sage);font-weight:700;font-size:19px;line-height:1.3;margin:36px 0 14px}
.offers .streams{display:flex;flex-direction:column;gap:8px;margin-top:14px}
.offers .streams .btn{text-align:left;display:flex;align-items:center;gap:10px;font-size:12px;letter-spacing:.5px}
.offers .streams svg{width:14px;height:14px}
.offers .offers-photo{position:absolute;left:0;bottom:0;width:100%;height:250px;clip-path:polygon(0 20%,100% 0,100% 100%,0 100%)}

.targets h2{font-size:18px;margin:36px 0 12px;line-height:1.25}
.targets h2.second{margin-top:18px}
.targets .elearn{position:absolute;left:30px;right:30px;bottom:30px;background:var(--sage);color:#fff;padding:18px 20px}
.targets .elearn h3{font-family:"Montserrat",Arial,sans-serif;font-size:16px;margin-bottom:8px}
.targets .elearn p{font-size:10.5px;line-height:1.55;margin-bottom:8px}
.targets .elearn ul{list-style:none;font-size:10.5px;line-height:1.5}
.targets .elearn li{display:flex;gap:8px;align-items:center;margin-bottom:3px}
.targets .elearn svg{width:12px;height:12px;flex:none}

.inperson{padding:0}
.inperson .inperson-photo{height:250px;width:100%}
.inperson .content{padding:22px 30px 0}
.inperson h2{font-size:17px;margin-bottom:10px}
.inperson .icons{list-style:none;font-size:10.5px;color:var(--muted);margin-bottom:18px}
.inperson .icons li{display:flex;gap:10px;align-items:center;margin-bottom:8px}
.inperson .icons svg{width:18px;height:18px;flex:none}
.inperson .footer{position:absolute;left:30px;right:30px;bottom:26px;display:flex;align-items:flex-end;justify-content:space-between}
.inperson .mini{background:var(--salmon);color:#fff;font-size:9px;padding:8px 10px;text-align:center;line-height:1.5}
.inperson .mini strong{display:block;font-size:10.5px}
.inperson .wordmark{font-size:18px;color:var(--sage);gap:6px}
.inperson .wordmark .dot{width:14px;height:14px}
</style>
</head>
<body>

<section class="spread outside">
  <div class="panel about">
    <div class="photo about-photo" role="img" aria-label="Black and white photo of several hands stacked together in teamwork"></div>
    <div class="about-band"></div>
    <div class="content">
      <h2><span>ABOUT</span>Brightmoor</h2>
      <p class="body">Brightmoor is an award-winning organisation providing dynamic and creative ways for children, young people, adults and families to make positive change and achieve fulfilling lives.</p>
      <p class="body">Our team has extensive experience working with individuals, families and services across the disability sector, delivering practical learning that makes a lasting difference.</p>
      <p class="body">Brightmoor's learning offering can be grouped into three core areas.</p>
      <span class="btn salmon">www.brightmoor.au</span>
    </div>
  </div>

  <div class="panel contact">
    <div class="quote">
      <div class="quote-mark">&ldquo;</div>
      <p>Brightmoor has given our staff the skills and confidence to provide person-centred support every single day.</p>
      <p>The training was engaging, relevant and easy to apply. Our team left with practical tools they now use with every client they support.</p>
      <p class="cite">&mdash; Service Manager, Disability Provider</p>
    </div>
    <div class="green">
      <div class="wordmark"><span class="dot"></span>Brightmoor</div>
      <div class="phone">03 9000 1234</div>
      <ul class="rows">
        <li><svg viewBox="0 0 20 20"><rect x="2" y="4" width="16" height="12" fill="none" stroke="#fff" stroke-width="1.6"/><path d="M2 5l8 6 8-6" fill="none" stroke="#fff" stroke-width="1.6"/></svg>info@brightmoor.au</li>
        <li><svg viewBox="0 0 20 20"><path d="M10 2a6 6 0 0 0-6 6c0 4.5 6 10 6 10s6-5.5 6-10a6 6 0 0 0-6-6z" fill="none" stroke="#fff" stroke-width="1.6"/><circle cx="10" cy="8" r="2" fill="#fff"/></svg>Level 2, 14 Harbour Street,<br>Northbay VIC 3000</li>
        <li><svg viewBox="0 0 20 20"><circle cx="10" cy="10" r="8" fill="none" stroke="#fff" stroke-width="1.6"/><path d="M2 10h16M10 2c3 3 3 13 0 16M10 2c-3 3-3 13 0 16" fill="none" stroke="#fff" stroke-width="1.3"/></svg>www.brightmoor.au</li>
      </ul>
      <div class="platform">BRIGHTMOOR'S eLEARNING PLATFORM</div>
      <span class="btn">elearning.brightmoor.au</span>
    </div>
  </div>

  <div class="panel cover">
    <div class="photo cover-photo" role="img" aria-label="Black and white photo of a woman and child sitting together on steps, seen from behind"></div>
    <div class="cover-band"></div>
    <div class="content">
      <div class="wordmark"><span class="dot"></span>Brightmoor</div>
      <h1>LEARNING<br>BROCHURE</h1>
      <div class="tag">SUPPORTING &amp; EMPOWERING</div>
    </div>
    <div class="foot">www.brightmoor.au</div>
  </div>
</section>

<section class="spread inside">
  <div class="panel offers">
    <p class="lead">Brightmoor offers a range of learning solutions focused on supporting and empowering individuals and organisations that support people with a range of disabilities</p>
    <p class="body">Our programs are designed and delivered by experienced clinicians and educators, drawing on current evidence and practice.</p>
    <p class="body">Learning is grouped into three streams:</p>
    <div class="streams">
      <span class="btn sage"><svg viewBox="0 0 14 14"><path d="M4 2l6 5-6 5z" fill="#fff"/></svg>eLearning</span>
      <span class="btn salmon"><svg viewBox="0 0 14 14"><path d="M4 2l6 5-6 5z" fill="#fff"/></svg>Face to Face Training</span>
      <span class="btn sage"><svg viewBox="0 0 14 14"><path d="M4 2l6 5-6 5z" fill="#fff"/></svg>Tailored Training Packages</span>
    </div>
    <div class="photo offers-photo" role="img" aria-label="Black and white photo of hands joined together in a star shape"></div>
  </div>

  <div class="panel targets">
    <h2>Our training solutions are targeted towards</h2>
    <ul class="list">
      <li>Families and carers</li>
      <li>Support workers and direct care workers</li>
      <li>Positive behaviour support practitioners</li>
      <li>Support coordinators, case managers and planners</li>
      <li>Frontline and customer service staff</li>
      <li>Allied health professionals</li>
      <li>Others working with and supporting people with a range of disabilities</li>
    </ul>
    <h2 class="second">The sectors we work in include</h2>
    <ul class="list">
      <li>Disability</li>
      <li>Mental health</li>
      <li>Health and community services</li>
      <li>Education</li>
      <li>Justice</li>
      <li>Clinical teams</li>
      <li>Other entities that are driving to be more inclusive</li>
    </ul>
    <div class="elearn">
      <h3>Brightmoor's eLearning</h3>
      <p>Our online courses offer flexible, self-paced learning that fits around your work and life.</p>
      <ul>
        <li><svg viewBox="0 0 12 12"><path d="M2 6l3 3 5-6" fill="none" stroke="#fff" stroke-width="1.8"/></svg>Positive behaviour support</li>
        <li><svg viewBox="0 0 12 12"><path d="M2 6l3 3 5-6" fill="none" stroke="#fff" stroke-width="1.8"/></svg>Understanding disability</li>
        <li><svg viewBox="0 0 12 12"><path d="M2 6l3 3 5-6" fill="none" stroke="#fff" stroke-width="1.8"/></svg>Communication and connection</li>
        <li><svg viewBox="0 0 12 12"><path d="M2 6l3 3 5-6" fill="none" stroke="#fff" stroke-width="1.8"/></svg>Introduction to person-centred practice</li>
      </ul>
    </div>
  </div>

  <div class="panel inperson">
    <div class="photo inperson-photo" role="img" aria-label="Black and white photo of a bright office entrance with glass doors"></div>
    <div class="content">
      <h2>In Person Training</h2>
      <ul class="icons">
        <li><svg viewBox="0 0 20 20"><path d="M10 2a6 6 0 0 0-6 6c0 4.5 6 10 6 10s6-5.5 6-10a6 6 0 0 0-6-6z" fill="var(--sage)"/><circle cx="10" cy="8" r="2" fill="#fff"/></svg>At our purpose-built training room or at your workplace</li>
        <li><svg viewBox="0 0 20 20"><rect x="3" y="4" width="14" height="13" fill="none" stroke="var(--sage)" stroke-width="1.8"/><path d="M3 8h14M7 2v4M13 2v4" stroke="var(--sage)" stroke-width="1.8"/></svg>Calendar of public sessions</li>
        <li><svg viewBox="0 0 20 20"><circle cx="10" cy="10" r="8" fill="var(--sage)"/><path d="M6 10l3 3 5-6" fill="none" stroke="#fff" stroke-width="1.8"/></svg>Bookings via the website</li>
      </ul>
      <h2>Tailored Training Packages</h2>
      <p class="body">Brightmoor develops customised in-house training programs for organisations and communities. Our tailored packages respond to your team's needs and goals.</p>
      <p class="body">Contact us to discuss a package that suits your service.</p>
    </div>
    <div class="footer">
      <div class="mini"><strong>Brightmoor's eLearning Platform</strong>elearning.brightmoor.au</div>
      <div class="wordmark"><span class="dot"></span>Brightmoor</div>
    </div>
  </div>
</section>

</body>
</html>
```